Community Legal Website

The website is about a law in legal area (Fiscal), it has a moderator and the community also contributes with information.

Attention that this is not for a Law Firm. This is a community site where all the lawyers can contribute wiith their knowledge and at the same time where they can read the Official Law in the fiscal area.

The site is in portuguese, but we have attach information in english about the functionalities.

I attach information which represents the first version of the site done by html.. That is the site we intend to improve.

The site is quite simple because the main pages are:
- Home page;
- Section page (which has the Chapters and articles)
- Article page;

This pages all belong to the article:

redaccao_actual.htm, redaccoes_anteriores.htm, anotacoes.htm, jurisprudencia.htm, decisoesadministrativas.htm, minutas.htm, duvidas.htm

AS you see in all of them the options are always there.

The most important in this site is the usability of the content:

The FAQ, Contacts, Terms of conditions, who we are, are links less important.

Also there is a possibility to have in the homepage a higligh of certain articles that we want to raise from the others.

Please check the excel sheet as well as the zip file wich has the site in portuguese that you can use a website translator to check in your language.
Updates

We added a excel sheet with the functionalities in english which the site must have.

Reason: Because this is easter time we have increased the time for the deliver

Please check briefing update.

Reason: There were some request to extend the deadline because of the Easter

Hi!

Please read carefully the briefing. People are presenting me company web sites adn this is NOT a company web site. THis is a Site wich has a content of Laws. Please check the 1st version in the zip file and improve it. The options are there and you can translate in google tradutor or reading the excel sheet attach.

txs,
JV

Reason: My client need more desing choices

Target Market(s)

Lawyers, jurists and people related with the fiscal Law.

Industry/Entity Type

Legal

Requirements
Must have
• The interface should be clean and elegant.
It should also contribute to speed.
And try to avoid to many distract elements.
The site will be dinamic and with a backoffice, so in that you have to be carefully with the space dynamic. But you don't have to worry about the backoffice. Only the front office which is the public site.

```html
<!DOCTYPE html>
<html lang="pt">
<head>
<meta charset="utf-8">
<title>Código do IRS - Artigo 32</title>
<link href="https://fonts.googleapis.com/css2?family=Open+Sans:wght@300;400;600;700&display=swap" rel="stylesheet">
<style>
:root{
  --ink:#2f3b3b;
  --teal:#2d6f6c;
  --teal-dark:#2c6a66;
  --muted:#8b9696;
  --cyan:#c1f9f6;
  --cyan-soft:#e2f8f7;
  --tab-bg:#b9cccb;
  --line:#dfe5e5;
  --strip:#f1f1f1;
  --footer:#5d7171;
  --white:#ffffff;
}
*{box-sizing:border-box;margin:0;padding:0}
html,body{width:1200px;height:636px;overflow:hidden;background:var(--white);font-family:"Open Sans",Arial,sans-serif;color:var(--ink)}
body{position:relative}
a{color:inherit;text-decoration:none;white-space:nowrap}
.site-header{height:60px;position:relative;border-bottom:1px solid #e4eaea}
.brand{position:absolute;left:294px;top:16px;display:flex;align-items:center;gap:20px;white-space:nowrap}
.brand-square{width:27px;height:27px;background:var(--teal-dark)}
.brand-name{font-weight:300;font-size:19px;color:#3d4f4f;letter-spacing:.2px}
.top-nav a{position:absolute;top:15px;height:31px;line-height:31px;font-size:9px;color:var(--muted);white-space:nowrap}
.top-nav a.active{background:var(--cyan);color:#3d5c5c;width:100px;text-align:center}
.article-band{height:83px;background:var(--cyan);position:relative}
.pager{position:absolute;top:34px;font-size:11.5px;color:#4f6666;display:flex;align-items:center;gap:8px;white-space:nowrap}
.pager.prev{left:25px}.pager.next{right:28px}
.article-title{position:absolute;left:0;right:0;top:13px;text-align:center;white-space:nowrap}
.article-title h1{font-weight:300;font-size:21px;color:#3b4c4c;line-height:28px}
.article-title p{font-weight:300;font-size:14px;color:#4f6868;line-height:20px;margin-top:1px}
.code-links{position:absolute;left:831px;top:12px;height:60px;width:76px;border-left:1px solid #9fd2cf;font-size:7px;color:var(--muted);line-height:12.3px;text-align:right;white-space:nowrap}
.code-links a{display:block}
.code-links a.current{color:#3d4f4f;text-decoration:underline}
.tab-band{height:35px;background:var(--cyan-soft);position:relative}
.tabs{position:absolute;left:294px;top:7px;width:612px;height:22px;background:var(--tab-bg);font-size:7.5px;color:#3d4f4f}
.tabs a{position:absolute;top:0;line-height:22px;height:22px;white-space:nowrap}
.tabs a.active{background:var(--teal);color:var(--white);font-weight:600;width:61px;text-align:center}
.tabs .comment{right:0;width:74px;background:#7fc6bf;display:flex;align-items:center;justify-content:space-between;padding:0 8px 0 10px}
.annotations{width:612px;margin:0 auto}
.note{margin-top:9px}
.note+.note{margin-top:20px}
.note-head{display:flex;justify-content:space-between;align-items:flex-start;border-bottom:1px solid var(--line);padding:0 12px 4px 14px;min-height:24px}
.note-head h2{font-weight:400;font-size:8.5px;color:var(--teal);line-height:12px;width:400px}
.note-meta{display:flex;font-size:7px;color:#6b7777;line-height:12px;white-space:nowrap}
.note-meta time{padding-right:9px;border-right:1px solid var(--line)}
.note-meta span{padding-left:9px}
.note-meta b{color:var(--teal);font-weight:700}
.note-body{font-size:6.6px;line-height:11.6px;padding:9px 14px 0 14px;color:#333}
.note-body p+p{margin-top:11px}
.note-foot{margin-top:10px;height:22px;background:var(--strip);display:flex;align-items:center;font-size:7px;color:#4b5b5b;white-space:nowrap}
.rate{padding-left:14px;display:flex;align-items:center;gap:5px}
.stars{display:flex;gap:2px;margin-left:4px}
.read-more{margin-left:auto;height:22px;background:#e1e1e1;width:150px;display:flex;align-items:center;justify-content:space-between;padding:0 8px 0 12px;color:#6a7575}
.bottom-links{position:absolute;top:515px;left:0;width:1200px;height:37px;background:#f4f4f4;border-top:1px solid #e2e2e2;display:flex;justify-content:flex-end;padding-right:306px;align-items:center;gap:14px;font-size:7.5px;color:var(--muted)}
.bottom-links a.current{color:#3d4f4f;text-decoration:underline}
.site-footer{position:absolute;top:552px;left:0;width:1200px;height:84px;background:var(--footer)}
.copyright{position:absolute;left:0;right:0;top:22px;text-align:center;font-size:6.5px;color:#e6eeee}
.contact-btn{position:absolute;left:806px;top:11px;width:100px;height:31px;background:var(--cyan);font-size:8.5px;color:#2f3b3b;display:flex;align-items:center;justify-content:center;gap:16px}
</style>
</head>
<body>
<header class="site-header">
  <a class="brand" href="#"><span class="brand-square"></span><span class="brand-name">TAVARES LOBO.net</span></a>
  <nav class="top-nav">
    <a class="active" href="#" style="left:574px">Termos de utilização</a>
    <a href="#" style="left:685px">Perguntas frequentes</a>
    <a href="#" style="left:793px">Quem somos</a>
    <a href="#" style="left:869px">Contactos</a>
  </nav>
</header>

<section class="article-band">
  <a class="pager prev" href="#"><svg width="9" height="14" viewBox="0 0 9 14"><path d="M7 1 1.5 7 7 13" fill="none" stroke="#4f6666" stroke-width="2"/></svg>Artigo anterior</a>
  <div class="article-title">
    <h1>CÓDIGO DO IRS - Artigo 32</h1>
    <p>Encargos não dedutíveis para efeitos fiscais</p>
  </div>
  <nav class="code-links">
    <a href="#">Índice deste Código</a>
    <a class="current" href="#">Menu dos Códigos</a>
    <a href="#">Gravar</a>
    <a href="#">Imprimir</a>
  </nav>
  <a class="pager next" href="#">Artigo seguinte<svg width="9" height="14" viewBox="0 0 9 14"><path d="M2 1 7.5 7 2 13" fill="none" stroke="#4f6666" stroke-width="2"/></svg></a>
</section>

<div class="tab-band">
  <nav class="tabs">
    <a href="#" style="left:13px">Redacção actual</a>
    <a href="#" style="left:94px">Redacções anteriores</a>
    <a class="active" href="#" style="left:176px">Anotações</a>
    <a href="#" style="left:243px">Jurisprudência</a>
    <a href="#" style="left:313px">Decisões administrativas</a>
    <a href="#" style="left:419px">Minutas</a>
    <a href="#" style="left:469px">Dúvidas</a>
    <a class="comment" href="#">COMENTAR<svg width="8" height="8" viewBox="0 0 8 8"><path d="M0 3h4V0l4 4-4 4V5H0z" fill="#2d6f6c"/></svg></a>
  </nav>
</div>

<main class="annotations">
  <article class="note">
    <div class="note-head">
      <h2>Como distinguir os encargos dedutíveis dos encargos parafiscais</h2>
      <div class="note-meta"><time>21.10.2012</time><span>Autor: <b>Tavares Lobo</b></span></div>
    </div>
    <div class="note-body">
      <p style="margin-top:4px">O penhor constitui um direito real de garantia que confere uma preferência ao credor pignoratício sobre coisas ou direitos não hipotecáveis.</p>
      <p>Esta figura jurídica encontra-se definida no n.º 1 do art.º 666.º do Código Civil, o qual dispõe que: "O penhor confere ao credor o direito à satisfação do seu crédito, bem como dos juros, se os houver, com preferência sobre os demais credores, pelo valor de certa coisa móvel, ou pelo valor de créditos ou outros direitos não susceptíveisalor de créditos ou outros direitos não susceptíveis de hipoteca, pertencentes ao devedor ou a ...</p>
    </div>
    <div class="note-foot">
      <div class="rate">Classificar:
        <span class="stars">
          <svg width="10" height="10" viewBox="0 0 10 10"><path d="M5 .3 6.4 3.4 9.8 3.7 7.2 6 8 9.4 5 7.6 2 9.4 2.8 6 .2 3.7 3.6 3.4z" fill="#2d6f6c"/></svg>
          <svg width="10" height="10" viewBox="0 0 10 10"><path d="M5 .3 6.4 3.4 9.8 3.7 7.2 6 8 9.4 5 7.6 2 9.4 2.8 6 .2 3.7 3.6 3.4z" fill="#2d6f6c"/></svg>
          <svg width="10" height="10" viewBox="0 0 10 10"><path d="M5 .3 6.4 3.4 9.8 3.7 7.2 6 8 9.4 5 7.6 2 9.4 2.8 6 .2 3.7 3.6 3.4z" fill="#2d6f6c"/></svg>
          <svg width="10" height="10" viewBox="0 0 10 10"><path d="M5 .3 6.4 3.4 9.8 3.7 7.2 6 8 9.4 5 7.6 2 9.4 2.8 6 .2 3.7 3.6 3.4z" fill="#2d6f6c"/></svg>
          <svg width="10" height="10" viewBox="0 0 10 10"><path d="M5 .3 6.4 3.4 9.8 3.7 7.2 6 8 9.4 5 7.6 2 9.4 2.8 6 .2 3.7 3.6 3.4z" fill="#2d6f6c"/></svg>
        </span>
      </div>
      <a class="read-more" href="#">Clique aqui para ler o texto integral<svg width="8" height="8" viewBox="0 0 8 8"><path d="M0 3h4V0l4 4-4 4V5H0z" fill="#a9b0b0"/></svg></a>
    </div>
  </article>

  <article class="note">
    <div class="note-head">
      <h2>Despesas fiscais com investimento: provisões, suprimentos, despesas com a própria empresa e remunerações variáveis</h2>
      <div class="note-meta"><time>18.10.2012</time><span>Autor: <b>Paulo Meireles</b></span></div>
    </div>
    <div class="note-body">
      <p style="margin-top:-4px">E isto porque é a Constituição que define e distribui as competências tributárias e que fixa os limites ao exercício do poder de tributar,limites que corúigum como verdadeiras garantias constitucionais do contribuinte, garante do justo equilíbrio entre o interesse do particular em.preservara sua esfera patrimonial. manifestação da sua liberdade, e o interesse do Fisco em assegurar para o Estado a cobertura das despesas públicas.</p>
      <p>Daí que, entre nós. se fale de uma "Constituição Fiscal", onde a legalidade tributária se configura como princípio fundamental que além de ser elemento essencial da distinção entre Finanças Públicas e Finanças Privadas. tem a dignidade constitucional de pressuposto r em.preservara sua esfera patrimonial. manifestação da sua liberdade, r em.preservara sua esfera patrimonial. patrimonial. patrimonial. ibutação, afirmando-se como a ...</p>
    </div>
    <div class="note-foot">
      <div class="rate">Classificar:
        <span class="stars">
          <svg width="10" height="10" viewBox="0 0 10 10"><path d="M5 .3 6.4 3.4 9.8 3.7 7.2 6 8 9.4 5 7.6 2 9.4 2.8 6 .2 3.7 3.6 3.4z" fill="#2d6f6c"/></svg>
          <svg width="10" height="10" viewBox="0 0 10 10"><path d="M5 .3 6.4 3.4 9.8 3.7 7.2 6 8 9.4 5 7.6 2 9.4 2.8 6 .2 3.7 3.6 3.4z" fill="#2d6f6c"/></svg>
          <svg width="10" height="10" viewBox="0 0 10 10"><path d="M5 .3 6.4 3.4 9.8 3.7 7.2 6 8 9.4 5 7.6 2 9.4 2.8 6 .2 3.7 3.6 3.4z" fill="#2d6f6c"/></svg>
          <svg width="10" height="10" viewBox="0 0 10 10"><path d="M5 .3 6.4 3.4 9.8 3.7 7.2 6 8 9.4 5 7.6 2 9.4 2.8 6 .2 3.7 3.6 3.4z" fill="#2d6f6c"/></svg>
          <svg width="10" height="10" viewBox="0 0 10 10"><path d="M5 .8 6.3 3.7 9.3 4 7 6 7.7 9 5 7.4 2.3 9 3 6 .7 4 3.7 3.7z" fill="none" stroke="#2d6f6c" stroke-width=".8"/></svg>
        </span>
      </div>
      <a class="read-more" href="#">Clique aqui para ler o texto integral<svg width="8" height="8" viewBox="0 0 8 8"><path d="M0 3h4V0l4 4-4 4V5H0z" fill="#a9b0b0"/></svg></a>
    </div>
  </article>
</main>

<nav class="bottom-links">
  <a href="#">Índice deste Código</a>
  <a class="current" href="#">Menu dos Códigos</a>
  <a href="#">Gravar</a>
  <a href="#">Imprimir</a>
</nav>

<footer class="site-footer">
  <p class="copyright">© TAVARES LOBO - 2013</p>
  <a class="contact-btn" href="#">CONTACT<svg width="13" height="9" viewBox="0 0 13 9"><rect x=".5" y=".5" width="12" height="8" fill="#3d4f4f"/><path d="M.5.5 6.5 5 12.5.5" fill="none" stroke="#c1f9f6" stroke-width="1"/></svg></a>
</footer>
</body>
</html>
```